Pain Management, Personal Injury & Motor Vehicle Accident

I need t rack card to use as marketing collateral while talking to urgent cares, wreckers services, primary care, and emergency room staff
If you have been involved in a motor vehicle accident or personal injury accident, Prairie Ridge Relief Clinic is your Solution to complete pain relief. We understand your pain and are here to assist you along the journey to becoming pain free. It is crucial that you choose a physician who is experienced in treating your unique injury.
At Prairie Ridge Relief Clinic, Dr Colin Marsh and his team of experts will provide you with a specialized approach to reducing and managing your pain with a comprehensive and effective treatment plan based on a proper diagnosis. You can expect an exceptional treatment program for your injuries to help you to begin improving your quality of life immediately.
We treat:
Car Accident Injuries
Semi Truck Injuries
Most Personal Injuries
Slip and Falls
Motorcycle Accident Injuries
Whiplash
Back Injuries
Neck Injuries
Shoulder Injuries
Headaches
Locations: Red Bend, Millbrook, Ashford
Phone: (580) 472-6193
Fax: (833) 718-2947
www.prairieridgerelief.example
Target Market(s)
Urgent Cares, Emergency Rooms, Primary Care, Wrecker Services, anyone involved in a Personal Injury or Motor Vehicle Accident
Industry/Entity Type
Healthcare, Motor Vehicle Accident Injury, Personal Injury, Pain Management, Pain Relief

```html
<!DOCTYPE html>
<html lang="en">
<head>
<meta charset="utf-8">
<title>Prairie Ridge Relief Clinic – Rack Card</title>
<link href="https://fonts.googleapis.com/css2?family=Montserrat:ital,wght@0,400;0,500;0,600;0,700;0,800;1,400;1,700&display=swap" rel="stylesheet">
<style>
  :root{
    --backdrop:#9a9a9c;
    --paper:#f1f1f2;
    --ink:#1c1c1c;
    --blue:#2a6db3;
    --blue-deep:#1f5d9f;
    --accent-red:#c0262d;
    --pill:#000;
    --white:#fff;
  }
  *{margin:0;padding:0;box-sizing:border-box}
  html,body{width:1074px;height:1200px;overflow:hidden}
  body{background:var(--backdrop);font-family:"Montserrat",sans-serif;color:var(--ink);position:relative}
  .card{position:absolute;top:73px;width:361px;height:1024px;background:var(--paper);overflow:hidden;box-shadow:0 6px 18px rgba(0,0,0,.35)}
  .card--front{left:128px}
  .card--back{left:563px}
  .abs{position:absolute}

  /* front */
  .brand{left:28px;top:86px;right:20px}
  .brand__mark{display:inline-block;width:14px;height:14px;border-radius:50%;background:var(--ink);vertical-align:middle;margin-right:6px}
  .brand__name{font-size:15px;font-weight:600;color:var(--ink);line-height:20px}
  .brand__line{height:1px;background:var(--accent-red);margin:4px 0 6px 20px}
  .brand__sub{font-size:10.5px;font-weight:600;margin-left:20px;line-height:15px}
  .hero-photo{left:0;top:175px;width:361px;height:355px;background:linear-gradient(180deg,#e6e6e6 0%,#9d9d9d 45%,#6a6a6a 75%,#b9b9b9 100%)}
  .hero-photo__glow{left:150px;top:180px;width:90px;height:150px;border-radius:50%;background:radial-gradient(closest-side,rgba(230,60,50,.8),rgba(230,60,50,0))}
  .inset-photo{width:148px;height:148px;border-radius:50%;border:4px solid var(--blue);box-shadow:0 8px 10px rgba(0,0,0,.2)}
  .inset-photo--exam{left:191px;top:400px;background:linear-gradient(160deg,#3cbec7 0%,#d9b8a8 45%,#6aa7d8 75%,#dfe6ee 100%)}
  .lead{left:28px;top:566px;font-size:17.5px;font-weight:500}
  .headline{left:30px;top:597px;font-size:27.5px;font-weight:800;line-height:32px;color:var(--blue);letter-spacing:.2px}
  .intro{left:30px;top:742px;font-size:14px;line-height:19.5px;white-space:nowrap}
  .intro b{font-weight:700}
  .note{left:30px;top:850px;width:300px;font-size:13.6px;line-height:18.6px;font-style:italic;font-weight:700}

  /* shared footer */
  .footer-band{left:0;top:944px;width:361px;height:80px;background:var(--blue)}
  .footer-rule{left:0;top:942px;width:361px;height:3px;background:var(--blue-deep)}
  .url-pill{left:28px;top:929px;width:298px;height:30px;border-radius:15px;background:var(--pill);border:2px solid var(--white);outline:1.5px solid var(--pill);color:var(--white);font-weight:700;font-size:15.5px;text-align:center;line-height:26px;letter-spacing:.2px}
  .phone{left:26px;top:966px;display:flex;align-items:center;gap:8px;color:var(--white);font-weight:700;font-size:34px;white-space:nowrap}
  .phone svg{width:34px;height:34px}

  /* back */
  .team-photo{left:0;top:0;width:361px;height:390px;background:linear-gradient(150deg,#eef0f1 0%,#dcdfe1 40%,#2b6d86 65%,#31455e 100%)}
  .inset-photo--doctor{left:195px;top:259px;background:linear-gradient(180deg,#c8ced3 0%,#dcb9a3 50%,#f4f6f8 100%)}
  .tagline{left:23px;top:412px;font-size:20px;font-weight:700;line-height:22px;color:var(--blue)}
  .tagline__rule{left:23px;top:463px;width:165px;height:3px;background:linear-gradient(90deg,var(--blue) 0 40%,#111 40% 100%)}
  .doctor{left:200px;top:425px;width:122px;text-align:right}
  .doctor__name{font-size:19px;font-weight:700;line-height:22px}
  .doctor__title{font-size:9px;line-height:11.5px;color:#333}
  .about{left:25px;top:481px;width:320px;font-size:13.3px;line-height:18.6px}
  .about i{font-style:italic}
  .about b{font-weight:700}
  .promise{left:25px;top:602px;width:320px;font-size:13.3px;line-height:18.6px}
  .promise strong{color:var(--blue);font-weight:700}
  .treat{left:20px;top:697px;width:323px;height:173px;border:1.5px solid var(--blue);border-radius:8px}
  .treat__title{position:absolute;left:50%;top:-12px;transform:translateX(-50%);background:var(--paper);padding:0 9px;font-size:17px;font-weight:700;color:var(--blue);white-space:nowrap}
  .treat__cols{display:flex;padding:22px 0 0 13px;gap:16px}
  .treat__list{list-style:none;width:150px}
  .treat__list li{position:relative;padding-left:13px;font-size:13.3px;line-height:18.4px;margin-bottom:2.3px}
  .treat__list li::before{content:"";position:absolute;left:1px;top:7px;width:4.5px;height:4.5px;border-radius:50%;background:var(--blue)}
  .locations{left:0;top:892px;width:361px;text-align:center;font-size:18px;font-weight:700;color:var(--blue);white-space:nowrap}
  .locations span{color:var(--ink);font-weight:400;margin:0 5px}
</style>
</head>
<body>

<section class="card card--front" aria-label="Rack card front">
  <div class="abs brand">
    <div class="brand__name"><span class="brand__mark"></span>Marsh Health, LLC dba<br><span style="margin-left:20px">Prairie Ridge Relief Clinic</span></div>
    <div class="brand__line"></div>
    <div class="brand__sub">Dr. Colin Marsh, MD</div>
  </div>

  <div class="abs hero-photo" role="img" aria-label="Photo of a man's bare back holding his lower back, spine highlighted in red">
    <div class="abs hero-photo__glow"></div>
  </div>
  <div class="abs inset-photo inset-photo--exam" role="img" aria-label="Photo of gloved hands examining a patient's lower back"></div>

  <p class="abs lead">If you have been involved in a</p>
  <h1 class="abs headline">MOTOR VEHICLE<br>ACCIDENT OR<br>PERSONAL INJURY<br>ACCIDENT,</h1>
  <p class="abs intro"><b>Prairie Ridge Relief Clinic</b> is<br>your Solution to complete pain relief.<br>We specialize in helping patients struggling<br>with pain and are here to assist you along<br>the journey to becoming pain free.</p>
  <p class="abs note">You want to choose a physician who is experienced in treating your unique injuries.</p>

  <div class="abs footer-rule"></div>
  <div class="abs footer-band"></div>
  <div class="abs url-pill">www.prairieridgerelief.example</div>
  <div class="abs phone">
    <svg viewBox="0 0 24 24" aria-hidden="true"><path fill="#fff" d="M6.6 10.8c1.4 2.8 3.8 5.2 6.6 6.6l2.2-2.2c.3-.3.7-.4 1-.2 1.1.4 2.3.6 3.6.6.6 0 1 .4 1 1V20c0 .6-.4 1-1 1C10.6 21 3 13.4 3 4c0-.6.4-1 1-1h3.5c.6 0 1 .4 1 1 0 1.3.2 2.5.6 3.6.1.3 0 .7-.2 1z"/><path fill="none" stroke="#fff" stroke-width="1.6" stroke-linecap="round" d="M14 3.5a7 7 0 0 1 6.5 6.5M14 7a3.5 3.5 0 0 1 3 3"/></svg>
    (580) 472-6193
  </div>
</section>

<section class="card card--back" aria-label="Rack card back">
  <div class="abs team-photo" role="img" aria-label="Photo of a physician with a tablet consulting a patient holding her shoulder in a clinic"></div>
  <div class="abs inset-photo inset-photo--doctor" role="img" aria-label="Portrait photo of Dr Colin Marsh in a white coat"></div>

  <h2 class="abs tagline">Relieving Pain<br>Improving Lives</h2>
  <div class="abs tagline__rule"></div>
  <div class="abs doctor">
    <div class="doctor__name">DR MARSH</div>
    <div class="doctor__title">Board Certified<br>Anesthesiologist</div>
  </div>

  <p class="abs about">At <i>Prairie Ridge Relief Clinic,</i><br><b>Dr Colin Marsh</b> and his experienced team will provide you with an individualized approach to reducing and managing your pain with a comprehensive and effective treatment plan based on a proper diagnosis.</p>
  <p class="abs promise">You can expect a <strong>5 star treatment plan</strong> for your injuries to help you begin <strong>improving your quality of life immediately.</strong></p>

  <div class="abs treat">
    <h3 class="treat__title">WE TREAT</h3>
    <div class="treat__cols">
      <ul class="treat__list">
        <li>Car Accident Injuries</li>
        <li>Semi Truck Injuries</li>
        <li>Most Personal Injuries</li>
        <li>Slip and Falls</li>
        <li>Back Injuries</li>
      </ul>
      <ul class="treat__list">
        <li>Motorcycle Accident Injuries</li>
        <li>Whiplash</li>
        <li>Neck Injuries</li>
        <li>Shoulder Injuries</li>
        <li>Headaches</li>
      </ul>
    </div>
  </div>

  <p class="abs locations">Red Bend<span>|</span>Millbrook<span>|</span>Ashford</p>

  <div class="abs footer-rule"></div>
  <div class="abs footer-band"></div>
  <div class="abs url-pill">www.prairieridgerelief.example</div>
  <div class="abs phone">
    <svg viewBox="0 0 24 24" aria-hidden="true"><path fill="#fff" d="M6.6 10.8c1.4 2.8 3.8 5.2 6.6 6.6l2.2-2.2c.3-.3.7-.4 1-.2 1.1.4 2.3.6 3.6.6.6 0 1 .4 1 1V20c0 .6-.4 1-1 1C10.6 21 3 13.4 3 4c0-.6.4-1 1-1h3.5c.6 0 1 .4 1 1 0 1.3.2 2.5.6 3.6.1.3 0 .7-.2 1z"/><path fill="none" stroke="#fff" stroke-width="1.6" stroke-linecap="round" d="M14 3.5a7 7 0 0 1 6.5 6.5M14 7a3.5 3.5 0 0 1 3 3"/></svg>
    (580) 472-6193
  </div>
</section>

</body>
</html>
```